Fitness Business Card Design Needed

We are looking for a business card design that stands out but is also simple and unique. I like the idea of on one side using the picture of myself with my logo at my feet. I love the texture on the business card so please take that into account when designing. Then on the other side having my contact details. I want it to be clean, modern, and pretty. I am open to designs that allow spot gloss or gold foiling.

Contact Information for Business Card

Space for Name, Phone number, email, and website

```html
<!DOCTYPE html>
<html lang="en">
<head>
<meta charset="utf-8">
<title>Petite Power Fitness – Business Card</title>
<link href="https://fonts.googleapis.com/css2?family=Montserrat:wght@300;400;500&display=swap" rel="stylesheet">
<style>
  :root {
    --backdrop: #2b2c30;
    --card: #141416;
    --card-edge: #1d1d20;
    --gold: #c9a25a;
    --text-light: #e6e6e6;
    --text-muted: #bfbfbf;
    --skin: #c99a7e;
    --swim: #d9543c;
    --sand: #cfc3b0;
  }
  * { margin: 0; padding: 0; box-sizing: border-box; }
  html, body { width: 1200px; height: 900px; overflow: hidden; }
  body {
    background: var(--backdrop);
    font-family: "Montserrat", sans-serif;
    position: relative;
  }
  .card {
    position: absolute;
    top: 135px;
    width: 360px;
    height: 630px;
    border-radius: 28px;
    background: radial-gradient(ellipse at 30% 20%, #1c1c1f 0%, var(--card) 70%);
    box-shadow: 0 0 0 1px var(--card-edge);
    overflow: hidden;
  }
  .card--contact { left: 180px; }
  .card--photo { left: 660px; }

  /* brand lockup */
  .brand {
    position: absolute;
    display: flex;
    flex-direction: column;
    align-items: center;
    gap: 12px;
    text-align: center;
  }
  .brand__mark {
    width: 40px;
    height: 40px;
    border: 1.5px solid var(--gold);
    flex-shrink: 0;
  }
  .brand__name {
    color: var(--gold);
    font-weight: 400;
    font-size: 14px;
    letter-spacing: 3px;
    line-height: 1.4;
    text-transform: uppercase;
    white-space: nowrap;
  }
  .card--contact .brand { top: 110px; left: 0; right: 0; }

  /* contact block */
  .contact {
    position: absolute;
    left: 42px;
    bottom: 70px;
  }
  .contact__name {
    color: var(--text-light);
    font-weight: 300;
    font-size: 30px;
    letter-spacing: 1px;
  }
  .contact__title {
    color: var(--gold);
    font-weight: 400;
    font-size: 17px;
    letter-spacing: 1px;
    margin: 4px 0 26px;
  }
  .contact__list { list-style: none; }
  .contact__item {
    display: flex;
    align-items: center;
    gap: 14px;
    color: var(--text-muted);
    font-size: 17px;
    font-weight: 400;
    margin-bottom: 14px;
  }
  .contact__icon { width: 18px; height: 18px; flex-shrink: 0; }

  /* photo side */
  .portrait {
    position: absolute;
    left: 30px;
    top: 20px;
    width: 180px;
    height: 610px;
    border-radius: 90px 90px 0 0;
    background: linear-gradient(180deg,
      #d8c3a6 0%, var(--skin) 22%, var(--swim) 38%, var(--skin) 50%,
      #b98a6d 78%, var(--sand) 92%, var(--sand) 100%);
    opacity: 0.9;
  }
  .card--photo .brand { top: 270px; left: 226px; width: 116px; }
  .card--photo .brand__name { font-size: 12px; letter-spacing: 2px; }
</style>
</head>
<body>

  <section class="card card--contact">
    <div class="brand">
      <span class="brand__mark"></span>
      <span class="brand__name">Petite Power<br>Fitness</span>
    </div>

    <div class="contact">
      <p class="contact__name">YOUR NAME</p>
      <p class="contact__title">JOB TITLE</p>
      <ul class="contact__list">
        <li class="contact__item">
          <svg class="contact__icon" viewBox="0 0 18 18"><rect x="4" y="1" width="10" height="16" rx="2" fill="none" stroke="var(--gold)" stroke-width="1.6"/><circle cx="9" cy="14" r="1" fill="var(--gold)"/></svg>
          000 000 0000
        </li>
        <li class="contact__item">
          <svg class="contact__icon" viewBox="0 0 18 18"><rect x="1" y="3" width="16" height="12" fill="var(--gold)"/><path d="M1 3 L9 10 L17 3" fill="none" stroke="var(--card)" stroke-width="1.4"/></svg>
          youremail@xyz.com
        </li>
        <li class="contact__item">
          <svg class="contact__icon" viewBox="0 0 18 18"><circle cx="9" cy="9" r="7.5" fill="none" stroke="var(--gold)" stroke-width="1.5"/><ellipse cx="9" cy="9" rx="3.2" ry="7.5" fill="none" stroke="var(--gold)" stroke-width="1.2"/><line x1="1.5" y1="9" x2="16.5" y2="9" stroke="var(--gold)" stroke-width="1.2"/></svg>
          www.yourwebsite.com
        </li>
      </ul>
    </div>
  </section>

  <section class="card card--photo">
    <div class="portrait" role="img" aria-label="Full-length photo of the trainer in a red swimsuit standing on a sandy rock"></div>
    <div class="brand">
      <span class="brand__mark"></span>
      <span class="brand__name">Petite<br>Power<br>Fitness</span>
    </div>
  </section>

</body>
</html>
```